Brambleton Business Card

I have a current card that I like it just needs a couple little changes to make it perfect. I would like the font size bigger so it could be easily read by older customers.

Business

```html
<!DOCTYPE html>
<html lang="en">
<head>
<meta charset="utf-8">
<title>Brambleton Motorsports and Marine – Business Card</title>
<link href="https://fonts.googleapis.com/css2?family=Questrial&family=Dancing+Script:wght@500&display=swap" rel="stylesheet">
<style>
  :root {
    --card-dark: #151515;
    --card-mid: #2b2b2b;
    --accent-green: #a9c27c;
    --text-light: #f2f2f2;
    --text-soft: #d9d9d9;
    --season-warm: #c9742e;
    --season-cool: #4f6e9a;
  }
  html, body {
    margin: 0;
    padding: 0;
    width: 1200px;
    height: 758px;
    overflow: hidden;
    background: var(--card-dark);
  }
  .business-card {
    position: relative;
    width: 1200px;
    height: 758px;
    background: radial-gradient(ellipse at 40% 45%, var(--card-mid) 0%, var(--card-dark) 75%);
    font-family: "Questrial", "Century Gothic", sans-serif;
    color: var(--text-light);
    overflow: hidden;
  }
  .company-header {
    position: absolute;
    left: 110px;
    top: 58px;
    width: 700px;
  }
  .company-name {
    margin: 0;
    font-weight: 400;
    font-size: 44px;
    letter-spacing: 0.5px;
    color: var(--accent-green);
  }
  .company-web {
    margin: 4px 0 0;
    text-align: right;
    font-size: 20px;
    color: var(--text-light);
  }
  .brand-mark {
    position: absolute;
    left: 120px;
    top: 250px;
    display: flex;
    align-items: center;
    gap: 22px;
  }
  .brand-dot {
    width: 56px;
    height: 56px;
    border-radius: 50%;
    background: var(--text-light);
  }
  .brand-word {
    font-size: 68px;
    color: var(--text-light);
    letter-spacing: 1px;
  }
  .contact-list {
    position: absolute;
    left: 760px;
    top: 200px;
    margin: 0;
    padding: 0;
    list-style: none;
    font-size: 23px;
    line-height: 1.4;
    color: var(--text-light);
  }
  .contact-label {
    color: var(--accent-green);
  }
  .seasons-emblem {
    position: absolute;
    left: 870px;
    top: 410px;
    width: 150px;
    height: 120px;
    border-radius: 50%;
    background: radial-gradient(circle at 40% 45%, var(--season-warm) 0%, #6e4a2a 45%, var(--season-cool) 80%, transparent 100%);
    opacity: 0.85;
  }
  .tagline {
    position: absolute;
    right: 90px;
    top: 570px;
    margin: 0;
    font-family: "Dancing Script", cursive;
    font-size: 46px;
    color: var(--text-light);
  }
  .person {
    position: absolute;
    left: 120px;
    top: 590px;
  }
  .person-name {
    margin: 0;
    font-size: 32px;
    font-weight: 400;
    color: var(--accent-green);
  }
  .person-email {
    margin: 2px 0 0;
    font-size: 23px;
    color: var(--text-light);
  }
</style>
</head>
<body>
  <main class="business-card">
    <header class="company-header">
      <h1 class="company-name">Brambleton Motorsports and Marine</h1>
      <p class="company-web">www.brambletonmotorsports.com</p>
    </header>

    <div class="brand-mark">
      <span class="brand-dot"></span>
      <span class="brand-word">Brambleton</span>
    </div>

    <ul class="contact-list">
      <li>555-014-2870 <span class="contact-label">phone</span></li>
      <li>555-014-2871 <span class="contact-label">fax</span></li>
      <li>4820 Orchard Lane</li>
      <li>Fairhaven, MN 55990</li>
    </ul>

    <div class="seasons-emblem" role="img" aria-label="Four-seasons emblem with sun, leaf and snowflake swirls"></div>

    <p class="tagline">fun for all seasons...</p>

    <section class="person">
      <h2 class="person-name">Dale Whitmore</h2>
      <p class="person-email">dale@brambletonmotorsports.com</p>
    </section>
  </main>
</body>
</html>
```